Austin Motivated Sellers #1

I am A local real estate investor in the highly competitive single family homes market of Austin,Tx.for fix and flipping My company uses several nontraditional and creative solutions for helping home owners sell their faster for cash with a closing date of their choice and helps them save thousands of dollars in having to pay real estate commissions and fees.My idea for the front of the postcard is to show the home owner what they could do with all the money they'll save by selling their home with us.I want a background picture on the front of taking a vacation with the money they'll save, or down payment on a new car on the back or even just a pile of cash they'll save to do whatever they like with.
Company name: Bold Harbor Properties
website: www.Quickdeedoffer.example
phone # : 512-555-0187 / 24hr.recorded message

Industry/Entity Type

Real Estate

```html
<!DOCTYPE html>
<html lang="en">
<head>
<meta charset="utf-8">
<title>Bold Harbor Properties – Postcard</title>
<link href="https://fonts.googleapis.com/css2?family=Source+Sans+3:ital,wght@0,400;0,600;0,700;1,400;1,600&family=PT+Sans+Narrow:wght@700&display=swap" rel="stylesheet">
<style>
  :root {
    --navy: #0d2a6b;
    --blue: #1a4d9e;
    --red: #b5202a;
    --white: #ffffff;
    --ink: #222222;
    --soft: #e9ecf1;
    --page: #ececec;
    --logo-blue: #1d3a86;
  }
  * { box-sizing: border-box; margin: 0; padding: 0; }
  html, body { width: 929px; height: 1200px; overflow: hidden; }
  body { background: var(--page); font-family: "Source Sans 3", sans-serif; position: relative; }

  .postcard {
    position: absolute; left: 102px; width: 721px; height: 487px;
    background: var(--white); overflow: hidden;
    box-shadow: 0 2px 6px rgba(0,0,0,.18);
  }
  .postcard--front { top: 78px; }
  .postcard--back { top: 642px; }
  .postcard__art { position: absolute; inset: 0; }
  .photo { position: absolute; }

  .headline { position: absolute; right: 19px; top: 24px; color: var(--white); font-size: 36px; font-weight: 400; letter-spacing: -0.5px; }
  .subhead { position: absolute; right: 19px; top: 75px; color: var(--white); font-size: 17.5px; font-weight: 400; }
  .rule { position: absolute; right: 22px; top: 109px; width: 173px; height: 3px; background: var(--white); }
  .pitch { position: absolute; right: 19px; top: 124px; text-align: right; color: var(--white); font-style: italic; font-size: 18.5px; line-height: 19px; }
  .benefits { position: absolute; right: 19px; top: 199px; list-style: none; color: var(--white); font-size: 13px; text-align: right; }
  .benefits li { height: 20px; line-height: 20px; display: flex; justify-content: flex-end; align-items: center; gap: 9px; }
  .benefits svg { width: 13px; height: 13px; }

  .brand { position: absolute; color: var(--logo-blue); font-weight: 600; text-align: center; line-height: 1.05; }
  .brand--front { left: 538px; top: 418px; width: 175px; font-size: 24px; }
  .brand--back { left: 20px; top: 78px; width: 190px; font-size: 24px; }

  .callout { position: absolute; left: 21px; color: var(--white); }
  .callout__note { font-size: 8.5px; }
  .callout__line { display: flex; align-items: center; gap: 10px; font-family: "PT Sans Narrow", sans-serif; font-weight: 700; font-size: 24px; letter-spacing: .4px; line-height: 28px; }
  .callout__line svg { width: 20px; height: 20px; margin-left: 8px; }
  .callout__web { font-size: 11.5px; letter-spacing: .5px; }
  .postcard--front .callout { top: 420px; }
  .postcard--back .callout { top: 425px; }

  .offer { position: absolute; left: 0; top: 143px; width: 330px; text-align: center; color: var(--white); font-size: 12px; line-height: 16px; }
  .offer__tag { margin-top: 5px; font-size: 12.5px; }
  .story { position: absolute; left: 16px; top: 222px; width: 150px; color: var(--ink); font-size: 9.6px; line-height: 11.4px; }

  .mailing { position: absolute; left: 421px; top: 38px; color: var(--ink); }
  .mailing__name { font-size: 13.5px; }
  .mailing__addr { margin-top: 6px; font-size: 11px; line-height: 14px; color: #333; }
  .stamp-box { position: absolute; left: 621px; top: 32px; width: 80px; height: 59px; border: 1px solid #888; }
  .address-line { position: absolute; left: 425px; width: 277px; height: 1px; background: #999; }
</style>
</head>
<body>

<!-- Front -->
<section class="postcard postcard--front">
  <div class="photo" role="img" aria-label="Smiling couple on a tropical beach with palm trees and sea" style="left:0;top:0;width:440px;height:487px;background:linear-gradient(160deg,#5aa6e0 0%,#9fd0ef 35%,#e8eef2 60%,#d9d4c8 100%);"></div>
  <svg class="postcard__art" viewBox="0 0 721 487" preserveAspectRatio="none">
    <defs>
      <linearGradient id="panelFront" x1="0" y1="0" x2="1" y2="1">
        <stop offset="0" stop-color="#1c4ea0"/><stop offset="1" stop-color="#0b2463"/>
      </linearGradient>
      <linearGradient id="bandFront" x1="0" y1="0" x2="1" y2="0">
        <stop offset="0" stop-color="#0d2a6b"/><stop offset="1" stop-color="#1e56a8"/>
      </linearGradient>
    </defs>
    <path d="M205 0 L721 0 L721 330 C600 345 480 382 415 442 C380 300 330 90 205 0 Z" fill="url(#panelFront)"/>
    <path d="M196 0 C318 80 372 280 408 446" fill="none" stroke="#fff" stroke-width="12"/>
    <path d="M204 0 C324 80 378 280 413 446" fill="none" stroke="var(--red)" stroke-width="5"/>
    <path d="M410 448 C480 380 600 338 721 322 L721 487 L395 487 Z" fill="#fff"/>
    <path d="M412 446 C482 380 602 338 721 323" fill="none" stroke="var(--red)" stroke-width="8"/>
    <path d="M0 396 C150 380 300 390 375 428 C400 448 415 468 430 487 L0 487 Z" fill="#fff"/>
    <path d="M0 402 C150 386 295 396 368 432 C392 450 407 468 420 487 L0 487 Z" fill="url(#bandFront)"/>
  </svg>

  <h1 class="headline">YOU NEED A VACATION?</h1>
  <p class="subhead">HERE'S HOW TO ACTUALLY SAVE UP FOR ONE</p>
  <div class="rule"></div>
  <p class="pitch">Take a vacation with the thousands you'll<br>save in fees and commissions when you<br>sell your home with us !</p>
  <ul class="benefits">
    <li>SELL YOUR HOME AS FAST AS 7 DAYS <svg viewBox="0 0 14 14"><rect x="1" y="2" width="10" height="10" rx="2" fill="none" stroke="#fff" stroke-width="1.4"/><path d="M4 7 L6.5 9.5 L13 2" fill="none" stroke="#fff" stroke-width="1.6"/></svg></li>
    <li>WE'LL BUY AS IS... NO REPAIRS NECESSARY <svg viewBox="0 0 14 14"><rect x="1" y="2" width="10" height="10" rx="2" fill="none" stroke="#fff" stroke-width="1.4"/><path d="M4 7 L6.5 9.5 L13 2" fill="none" stroke="#fff" stroke-width="1.6"/></svg></li>
    <li>WE PAY CASH FOR YOUR PROPERTY <svg viewBox="0 0 14 14"><rect x="1" y="2" width="10" height="10" rx="2" fill="none" stroke="#fff" stroke-width="1.4"/><path d="M4 7 L6.5 9.5 L13 2" fill="none" stroke="#fff" stroke-width="1.6"/></svg></li>
    <li>CLOSING DATE OF YOUR CHOICE <svg viewBox="0 0 14 14"><rect x="1" y="2" width="10" height="10" rx="2" fill="none" stroke="#fff" stroke-width="1.4"/><path d="M4 7 L6.5 9.5 L13 2" fill="none" stroke="#fff" stroke-width="1.6"/></svg></li>
    <li>SAVE THOUSANDS OF DOLLARS <svg viewBox="0 0 14 14"><rect x="1" y="2" width="10" height="10" rx="2" fill="none" stroke="#fff" stroke-width="1.4"/><path d="M4 7 L6.5 9.5 L13 2" fill="none" stroke="#fff" stroke-width="1.6"/></svg></li>
    <li>NO COMMISSIONS TO BE PAID <svg viewBox="0 0 14 14"><rect x="1" y="2" width="10" height="10" rx="2" fill="none" stroke="#fff" stroke-width="1.4"/><path d="M4 7 L6.5 9.5 L13 2" fill="none" stroke="#fff" stroke-width="1.6"/></svg></li>
  </ul>

  <p class="brand brand--front">Lone Oak<br>Home Buyer</p>

  <div class="callout">
    <p class="callout__note">24hr.Recorded message</p>
    <p class="callout__line">CALL NOW <svg viewBox="0 0 20 20"><circle cx="10" cy="10" r="8.5" fill="none" stroke="#fff" stroke-width="2"/><path d="M6.5 5.5 L8.3 5.2 L9 7.8 L7.9 8.6 C8.5 10 9.7 11.3 11.2 12 L12 10.9 L14.6 11.6 L14.3 13.4 C10 13.6 6.3 10 6.5 5.5 Z" fill="#fff"/></svg> 512-555-0187</p>
    <p class="callout__web">www.Quickdeedoffer.example</p>
  </div>
</section>

<!-- Back -->
<section class="postcard postcard--back">
  <svg class="postcard__art" viewBox="0 0 721 487" preserveAspectRatio="none">
    <defs>
      <linearGradient id="panelBack" x1="0" y1="0" x2="0" y2="1">
        <stop offset="0" stop-color="#f3f4f6"/><stop offset="1" stop-color="#e3e5ea"/>
      </linearGradient>
      <linearGradient id="bandBack" x1="0" y1="0" x2="1" y2="0">
        <stop offset="0" stop-color="#0d2a6b"/><stop offset="1" stop-color="#1e56a8"/>
      </linearGradient>
    </defs>
    <path d="M0 0 L206 0 C322 80 372 280 408 487 L0 487 Z" fill="url(#panelBack)"/>
    <path d="M0 138 L308 138 C318 160 326 185 332 210 L0 210 Z" fill="url(#bandBack)"/>
    <path d="M212 0 C328 80 382 280 420 478" fill="none" stroke="var(--red)" stroke-width="8"/>
    <path d="M0 404 C150 388 300 398 372 432 C396 450 410 468 424 487 L0 487 Z" fill="#fff"/>
    <path d="M0 410 C150 394 295 404 365 436 C388 452 402 470 414 487 L0 487 Z" fill="url(#bandBack)"/>
  </svg>
  <div class="photo" role="img" aria-label="Excited young couple holding a fan of cash in front of a new white car" style="left:172px;top:222px;width:192px;height:183px;background:linear-gradient(135deg,#dfe3e8 0%,#c9ced6 45%,#c98a5e 75%,#d2452f 100%);border-radius:0 0 40px 0;"></div>

  <p class="brand brand--back">Lone Oak<br>Home Buyer</p>

  <div class="offer">
    <p>You could save thousands selling your home with us<br>Use the money for a down payment on a new car!</p>
    <p class="offer__tag">WE BUY PROPERTIES FAST...</p>
  </div>

  <p class="story">We Buy Properties Fast... regardless of condition, equity, or situation. We've handled just about every situation you can imagine. We buy with cash. We even have many creative solutions available. We are the experts and you could save thousands selling your house with us!</p>

  <div class="callout">
    <p class="callout__note">24hr.Recorded message</p>
    <p class="callout__line">CALL NOW <svg viewBox="0 0 20 20"><circle cx="10" cy="10" r="8.5" fill="none" stroke="#fff" stroke-width="2"/><path d="M6.5 5.5 L8.3 5.2 L9 7.8 L7.9 8.6 C8.5 10 9.7 11.3 11.2 12 L12 10.9 L14.6 11.6 L14.3 13.4 C10 13.6 6.3 10 6.5 5.5 Z" fill="#fff"/></svg> 512-555-0187</p>
    <p class="callout__web">www.Quickdeedoffer.example</p>
  </div>

  <div class="mailing">
    <p class="mailing__name">Bold Harbor Properties</p>
    <p class="mailing__addr">1420 Elm Ridge Rd., Ste.<br>Austin, TX, 78701</p>
  </div>
  <div class="stamp-box"></div>
  <div class="address-line" style="top:169px"></div>
  <div class="address-line" style="top:216px"></div>
  <div class="address-line" style="top:263px"></div>
  <div class="address-line" style="top:310px"></div>
</section>

</body>
</html>
```